2026 Varnex Loprin LWB Vehicle Wrap Design for Ridgeway Electrical and Refrigeration Work Vans

We are Ridgeway Electrical and Refrigeration — a Perth-based commercial electrical, air conditioning and refrigeration company. We service commercial buildings, homes and luxury residential jobs across the metro area and remote WA.
We need a clean, professional and high-impact full vehicle wrap design for our work vans. The vans are our mobile billboards, so the design needs to look sharp from a distance, communicate trust and competence, and clearly show what we do.
Must include:

Our company name: Ridgeway Electrical and Refrigeration
Tagline options (you can choose the strongest placement or suggest alternatives):
“Electrical | Air Conditioning | Refrigeration – Perth & Remote WA”
Licence numbers "AU051237 and EC24813"
Phone number: 0491 538 214
Website: ridgewayelectricalrefrigeration.com.au
Email: admin@ridgewayelectricalrefrigeration.com.au
Our existing logo (will be uploaded)

Style we want:

Professional, modern and trustworthy
Bold enough to stand out on the road but not flashy or overly busy
Clean hierarchy so the company name and phone number are readable at speed
Strong use of contrast

Colour preferences:

Prefer designs that work with our existing branding (we will upload the logo and brand colours)
Open to strong, professional colour combinations (navy/dark blue, black, white, and one accent colour such as orange, red or electric blue often work well in the trades)

Avoid:

Cluttered designs with too much text
Cartoonish or overly “tradie” looking graphics
Designs that look cheap or dated

Additional notes:

Design should scale well so we can use the same concept across multiple vans
We will need print-ready files (high-res, layered) at the end

Please upload your best concepts. We will give clear feedback and work with the winning designer to refine the final artwork for production.

Target Market(s)

commercial buildings, homes and luxury residential jobs across the metro area and remote WA.

Industry/Entity Type

Electrical, Air Conditioning and Refrigeration

Colors
0054AA
0677BA
7BADD7
CADEEF
E8F1F8

Requirements
Must have
• Our company name: Ridgeway Electrical and Refrigeration Tagline options (you can choose the strongest placement or suggest alternatives): “Electrical | Air Conditioning | Refrigeration – Perth & Remote WA” Licence numbers "AU051237 and EC24813" Phone number: 0491 538 214 Website: ridgewayelectricalrefrigeration.com.au Email: admin@ridgewayelectricalrefrigeration.com.au Our existing logo (will be uploaded)
Nice to have
• Professional, modern and trustworthy Bold enough to stand out on the road but not flashy or overly busy Clean hierarchy so the company name and phone number are readable at speed Strong use of contrast
Should not have
• Cluttered designs with too much text Cartoonish or overly “tradie” looking graphics Designs that look cheap or dated

```html
<!DOCTYPE html>
<html lang="en">
<head>
<meta charset="utf-8">
<title>Ridgeway Electrical and Refrigeration – Van Wrap</title>
<link rel="stylesheet" href="https://fonts.googleapis.com/css2?family=Montserrat:wght@600;700;800&display=swap">
<style>
  :root {
    --brand-blue: #0a5fd6;
    --deep-blue: #0036e0;
    --mid-blue: #0677ba;
    --aqua: #00c8e0;
    --panel: #f4f4f2;
    --white: #ffffff;
  }
  * { margin: 0; padding: 0; box-sizing: border-box; }
  html, body {
    width: 1200px; height: 662px; overflow: hidden;
    background: var(--white);
    font-family: "Montserrat", sans-serif;
  }
  .wrap {
    position: relative; width: 1200px; height: 662px;
    background: var(--panel);
  }
  .sweep {
    position: absolute; inset: 0;
    width: 1200px; height: 662px;
  }
  .brand {
    position: absolute; left: 132px; top: 224px;
    display: flex; align-items: flex-start; gap: 14px;
  }
  .brand-square {
    width: 82px; height: 80px; background: var(--brand-blue);
    flex: none;
  }
  .brand-name {
    color: var(--brand-blue); font-weight: 700;
    font-size: 22px; line-height: 22px; letter-spacing: 0.8px;
    text-transform: uppercase; white-space: nowrap;
    margin-top: 1px;
  }
  .tagline {
    position: absolute; left: 229px; top: 293px;
    color: var(--brand-blue); font-weight: 700; font-size: 8px; line-height: 10px;
    letter-spacing: 0.2px; white-space: nowrap;
  }
  .licence {
    position: absolute; left: 132px; top: 314px;
    height: 22px; padding: 0 12px 0 8px;
    border-radius: 11px;
    background: linear-gradient(90deg, var(--brand-blue), var(--aqua));
    color: var(--white); font-weight: 700; font-size: 16px; line-height: 22px;
    letter-spacing: 0.5px; white-space: nowrap;
  }
  .phone {
    position: absolute; left: 524px; top: 368px;
    display: flex; align-items: center; gap: 8px;
    color: var(--white); font-weight: 700; font-size: 39px;
    letter-spacing: 1.5px; white-space: nowrap;
  }
  .phone svg { width: 30px; height: 42px; }
  .contact {
    position: absolute; right: 331px; top: 418px;
    text-align: right; color: var(--white);
    font-weight: 600; font-size: 11px; line-height: 15px;
    letter-spacing: 0.3px; white-space: nowrap;
  }
</style>
</head>
<body>
<main class="wrap">
  <svg class="sweep" viewBox="0 0 1200 662" role="img" aria-label="Blue to aqua brush stroke sweep across the van side">
    <defs>
      <linearGradient id="sweepGradient" x1="0" y1="0" x2="1" y2="0">
        <stop offset="0" stop-color="#0030e0"/>
        <stop offset="0.55" stop-color="#0677d8"/>
        <stop offset="1" stop-color="#00d2e0"/>
      </linearGradient>
    </defs>
    <path d="M640 240 L1200 240 L1200 540 L420 540 L470 470 L440 430 L520 400 L480 360 L560 330 L590 290 L620 270 Z" fill="url(#sweepGradient)"/>
  </svg>

  <div class="brand">
    <div class="brand-square" aria-hidden="true"></div>
    <h1 class="brand-name">Ridgeway<br>Electrical &amp;<br>Refrigeration</h1>
  </div>
  <p class="tagline">Electrical ● Air Conditioning ● Refrigeration ● Perth &amp; Remote WA</p>

  <p class="licence">AU051237 &amp; EC24813</p>

  <p class="phone">
    <svg viewBox="0 0 24 34" aria-hidden="true">
      <path d="M6 2 L10 2 L12 10 L9 12 C9 18 12 23 16 25 L19 22 L24 27 L21 32 C10 32 2 20 3 6 Z" fill="#ffffff"/>
    </svg>
    0491 538 214
  </p>

  <p class="contact">ridgewayelectricalrefrigeration.com.au<br>admin@ridgewayelectricalrefrigeration.com.au</p>
</main>
</body>
</html>
```